Furniture & Lighting Wholesaler Needs a Product Catalogue/Look Book

Our company, Voreth Supply Co, imports quality hand-made furniture, lighting and decor from South Africa. Our products are well-designed and are designed to be used in up-market hotels and homes. Our primary customers are small- to medium-size retail shops.
We require a +/- 14-16 page look book (concept as per attached image) that will be used both in hard-copy and online. We have all of the necessary high-res images, descriptions/text etc. We need you to propose several design concepts from which we can choose, and then execute the design.
Please visit our website www.vorethsupply-example.com to see the products and their descriptions, as well as to get a feel for our style. Thank you for looking at our project!
Target Market(s)
Boutique Furniture Stores; Interior Designers
Other font styles liked:
- Bauer Bodini and Open Sans Condensed

```html
<!DOCTYPE html>
<html lang="en">
<head>
<meta charset="utf-8">
<title>Voreth Supply Co – Look Book Spread</title>
<link rel="stylesheet" href="https://fonts.googleapis.com/css2?family=Montserrat:wght@400;600;700&family=Open+Sans:wght@400;600&display=swap">
<style>
  :root {
    --backdrop: #d3d3d3;
    --paper: #f6f6f4;
    --gold: #a89a6c;
    --gold-dark: #8e8155;
    --charcoal: #3f3f3f;
    --ink: #2b2b2b;
    --muted: #6b6b6b;
    --rule: #d8d8d4;
    --photo-light: #e4e6e2;
    --photo-mid: #a9aea6;
  }
  * { margin: 0; padding: 0; box-sizing: border-box; }
  html, body { width: 1200px; height: 800px; overflow: hidden; }
  body { background: var(--backdrop); font-family: "Open Sans", sans-serif; color: var(--ink); position: relative; }

  .spread { position: absolute; left: 40px; top: 100px; width: 1120px; height: 600px; box-shadow: 0 6px 24px rgba(0,0,0,.18); }
  .page { position: absolute; top: 0; width: 560px; height: 600px; background: var(--paper); overflow: hidden; }
  .page--left { left: 0; }
  .page--right { left: 560px; }
  .gutter { position: absolute; left: 550px; top: 0; width: 20px; height: 600px; background: linear-gradient(90deg, rgba(0,0,0,0), rgba(0,0,0,.08) 50%, rgba(0,0,0,0)); z-index: 3; pointer-events: none; }

  .product-title { font-family: "Montserrat", sans-serif; font-weight: 400; color: var(--gold); font-size: 34px; line-height: 1; letter-spacing: 1px; text-transform: uppercase; }
  .product-intro { font-family: "Montserrat", sans-serif; font-size: 10.5px; line-height: 1.45; color: var(--ink); margin-top: 12px; width: 230px; }

  .price-tag { position: relative; width: 180px; height: 64px; margin-top: 26px; margin-left: 34px; }
  .price-tag::before { content: ""; position: absolute; left: -8px; top: 8px; width: 180px; height: 64px; background: var(--charcoal); }
  .price-tag__value { position: absolute; inset: 0; background: var(--gold); color: #fff; font-family: "Montserrat", sans-serif; font-size: 30px; display: flex; align-items: center; justify-content: center; letter-spacing: 1px; }

  .section-rule { height: 1px; background: var(--rule); margin-top: 24px; width: 240px; }
  .features__heading { font-family: "Montserrat", sans-serif; font-weight: 700; font-size: 11.5px; margin-top: 12px; }
  .features__list { list-style: none; margin-top: 6px; }
  .features__list li { font-size: 8.5px; line-height: 1.6; color: var(--muted); padding-left: 10px; position: relative; }
  .features__list li::before { content: ""; position: absolute; left: 0; top: 6px; width: 3px; height: 3px; border-radius: 50%; background: var(--muted); }

  .copy-column { position: absolute; }
  .page--left .copy-column { left: 42px; top: 70px; }
  .page--right .copy-column { left: 280px; top: 34px; }

  .edge-tab { position: absolute; width: 30px; background: var(--gold); }
  .edge-tab--left { left: 0; top: 330px; height: 270px; border-top-right-radius: 30px; }
  .edge-tab--right { right: 0; top: 0; height: 250px; border-bottom-left-radius: 30px; }
  .page-number { position: absolute; width: 30px; height: 34px; background: var(--charcoal); color: #c9c9c9; font-size: 9px; display: flex; align-items: center; justify-content: center; }
  .edge-tab--left .page-number { bottom: 0; left: 0; border-top-right-radius: 12px; }
  .edge-tab--right .page-number { bottom: 0; left: 0; border-top-left-radius: 12px; }

  .hero-frame { position: absolute; left: 320px; top: 0; width: 480px; height: 330px; border: 1.5px solid var(--gold); border-top: none; border-radius: 0 0 22px 22px; background: #fff; z-index: 2; overflow: hidden; display: flex; }
  .hero-shadow { position: absolute; left: 306px; top: 0; width: 508px; height: 346px; background: #e3e3e0; border-radius: 0 0 34px 34px; z-index: 1; }
  .hero-photo { flex: 1; margin: 30px 20px; border-radius: 8px; background: radial-gradient(ellipse at 50% 55%, var(--photo-mid) 0%, var(--photo-light) 65%, #fff 100%); }

  .gallery { position: absolute; }
  .gallery__heading { font-family: "Montserrat", sans-serif; font-weight: 700; font-size: 11.5px; }
  .gallery__row { display: flex; gap: 10px; margin-top: 10px; }
  .gallery__thumb { width: 76px; height: 76px; background: #fff; border: 1px solid #ececea; display: flex; align-items: center; justify-content: center; }
  .gallery__thumb span { display: block; width: 56px; height: 60px; border-radius: 6px; }
  .thumb--striped { background: linear-gradient(160deg, #5a5a58, #b9b9b5); }
  .thumb--grey { background: linear-gradient(160deg, #7f857d, #cfd2cc); }
  .page--left .gallery { left: 330px; top: 354px; }
  .page--right .gallery { left: 280px; top: 330px; }

  .below-frame { position: absolute; left: 40px; top: 350px; }

  .site-footer { position: absolute; bottom: 18px; display: flex; align-items: center; gap: 8px; background: #ebebe8; border-radius: 12px; padding: 5px 12px; font-size: 8px; color: var(--muted); }
  .site-footer__mark { width: 10px; height: 10px; border: 1.5px solid var(--charcoal); }
  .page--left .site-footer { right: 24px; }
  .page--right .site-footer { left: 40px; }
</style>
</head>
<body>
<div class="spread">
  <div class="hero-shadow"></div>
  <div class="hero-frame">
    <div class="hero-photo" role="img" aria-label="Manhattan Chair, front view photograph"></div>
    <div class="hero-photo" role="img" aria-label="Manhattan Chair, angled view photograph"></div>
  </div>

  <section class="page page--left">
    <div class="copy-column">
      <h1 class="product-title">Manhattan<br>Chair</h1>
      <p class="product-intro">Facculpa ipilm excearum rae expligent lam qui occulpa rchicie ndesequ laturita evero et, tem dolestiae.Odio blaborehent pra voluptas voloreri dolupta dendam.</p>
      <div class="price-tag"><div class="price-tag__value">$1,750</div></div>
      <div class="section-rule"></div>
      <h2 class="features__heading">Product Features</h2>
      <ul class="features__list">
        <li>Sint labor simvelluptat ulles erspellacil</li>
        <li>Es maximus si num ad etus</li>
        <li>Acerersped moluptaquate</li>
        <li>Eelia cus cuptatem voles</li>
        <li>Bos es doluptam inverchicils</li>
        <li>Wuidi dollorestrum</li>
        <li>Cus de nones mos ma idit res magnam</li>
        <li>Aut que ex enist fugitio restrunt</li>
      </ul>
    </div>
    <div class="edge-tab edge-tab--left"><div class="page-number">4</div></div>
    <div class="gallery">
      <h2 class="gallery__heading">Images of Products</h2>
      <div class="gallery__row">
        <div class="gallery__thumb"><span class="thumb--striped" role="img" aria-label="Striped armchair photograph"></span></div>
        <div class="gallery__thumb"><span class="thumb--striped" role="img" aria-label="Patterned chair back photograph"></span></div>
        <div class="gallery__thumb"><span class="thumb--grey" role="img" aria-label="Grey upholstered chair photograph"></span></div>
      </div>
    </div>
    <div class="site-footer"><span class="site-footer__mark"></span>www.vorethsupply-example.com</div>
  </section>

  <section class="page page--right">
    <div class="below-frame">
      <h2 class="features__heading">Product Features</h2>
      <ul class="features__list">
        <li>Sint labor simvelluptat ulles erspellacil</li>
        <li>Es maximus si num ad etus</li>
        <li>Acerersped moluptaquate</li>
        <li>Eelia cus cuptatem voles</li>
        <li>Bos es doluptam inverchicils</li>
        <li>Wuidi dollorestrum</li>
        <li>Cus de nones mos ma idit res magnam</li>
        <li>Aut que ex enist fugitio restrunt</li>
      </ul>
    </div>
    <div class="copy-column">
      <h1 class="product-title">Manhattan<br>Chair</h1>
      <p class="product-intro">Facculpa ipilm excearum rae expligent lam qui occulpa rchicie ndesequ laturita evero et, tem dolestiae.Odio blaborehent pra voluptas voloreri dolupta dendam.</p>
      <div class="price-tag"><div class="price-tag__value">$1,750</div></div>
    </div>
    <div class="gallery">
      <h2 class="gallery__heading">Images of Products</h2>
      <div class="gallery__row">
        <div class="gallery__thumb"><span class="thumb--striped" role="img" aria-label="Striped armchair photograph"></span></div>
        <div class="gallery__thumb"><span class="thumb--striped" role="img" aria-label="Patterned chair back photograph"></span></div>
        <div class="gallery__thumb"><span class="thumb--grey" role="img" aria-label="Grey upholstered chair photograph"></span></div>
      </div>
    </div>
    <div class="edge-tab edge-tab--right"><div class="page-number">5</div></div>
    <div class="site-footer"><span class="site-footer__mark"></span>www.vorethsupply-example.com</div>
  </section>

  <div class="gutter"></div>
</div>
</body>
</html>
```